" Somos dois amigos que decidiram juntar talentos fotográficos numa empresa cujo objetivo é fotografar adultos: casamentos, ensaio sensual, festas de aniversário e, ainda, ensaios de moda. "

```html
<!DOCTYPE html>
<html lang="pt-BR">
<head>
<meta charset="utf-8">
<title>Lumina – cartões de visita</title>
<link href="https://fonts.googleapis.com/css2?family=Arimo:wght@400;700&display=swap" rel="stylesheet">
<style>
  :root {
    --page: #ecebe8;
    --card-dark: #2b2c2a;
    --card-dark-gloss: #3c3d3b;
    --card-light: #ffffff;
    --band: #050505;
    --ink-grey: #7a7a7a;
    --ink-soft: #9a9a9a;
    --ink-light: #ffffff;
    --band-muted: #8a8a8a;
    --tile-light: #f2f2f2;
    --tile-shade: #bdbdbd;
  }
  * { margin: 0; padding: 0; box-sizing: border-box; }
  html, body { width: 1200px; height: 1200px; overflow: hidden; }
  body {
    background: var(--page);
    font-family: "Arimo", Arial, sans-serif;
    position: relative;
  }
  .card {
    position: absolute;
    width: 540px;
    height: 540px;
    overflow: hidden;
    box-shadow: 0 6px 18px rgba(0,0,0,0.18);
  }
  .card--front {
    left: 48px;
    background: var(--card-dark);
    border-radius: 30px 0 80px 0;
  }
  .card--front.card--glossy {
    background: linear-gradient(135deg, #1e1f1d 0%, #2a2b29 49.8%, var(--card-dark-gloss) 50.2%, #2a2b29 100%);
  }
  .card--back {
    left: 629px;
    background: var(--card-light);
    border-radius: 0 80px 0 80px;
  }
  .row-top { top: 48px; }
  .row-bottom { top: 629px; }

  .tile-cluster {
    position: absolute;
    left: 40px;
    top: 30px;
    width: 330px;
    height: 300px;
    background: radial-gradient(ellipse at 40% 45%, var(--tile-light) 0%, var(--tile-shade) 45%, rgba(43,44,42,0) 75%);
    opacity: 0.85;
  }

  .brand {
    position: absolute;
    left: 200px;
    top: 372px;
    display: flex;
    align-items: center;
    gap: 14px;
  }
  .brand__dot {
    width: 16px; height: 16px; border-radius: 50%;
    background: var(--ink-grey);
  }
  .brand__name {
    font-size: 44px;
    font-weight: 400;
    letter-spacing: 4px;
    color: var(--ink-soft);
  }
  .brand__tag {
    position: absolute;
    left: 262px;
    top: 430px;
    font-size: 11px;
    letter-spacing: 6px;
    color: var(--ink-grey);
  }

  .person {
    position: absolute;
    left: 0; right: 0;
    top: 172px;
    text-align: center;
  }
  .person__name {
    font-weight: 700;
    font-size: 38px;
    color: var(--ink-grey);
    letter-spacing: 0.5px;
  }
  .person__role {
    margin-top: 12px;
    font-size: 20px;
    letter-spacing: 7px;
    color: #222;
  }
  .contact-band {
    position: absolute;
    left: 0; right: 0; bottom: 0;
    height: 175px;
    background: var(--band);
    padding: 30px 34px 0 0;
    text-align: right;
    color: var(--ink-light);
    font-size: 21px;
    line-height: 1;
  }
  .contact-band p + p { margin-top: 22px; }
  .contact-band .site { color: var(--band-muted); font-size: 22px; }
</style>
</head>
<body>
  <section class="card card--front row-top">
    <div class="tile-cluster" role="img" aria-label="Composição decorativa de quadrados claros sobrepostos"></div>
    <div class="brand"><span class="brand__dot"></span><span class="brand__name">LUMINA</span></div>
    <p class="brand__tag">fotografia</p>
  </section>

  <section class="card card--back row-top">
    <div class="person">
      <h1 class="person__name">RAFAEL DUARTE</h1>
      <p class="person__role">fotógrafo</p>
    </div>
    <div class="contact-band">
      <p>rafael.duarte@luminafoto.com.br</p>
      <p>(XX) 99999.99999</p>
      <p class="site">luminafoto.com.br</p>
    </div>
  </section>

  <section class="card card--front card--glossy row-bottom">
    <div class="tile-cluster" role="img" aria-label="Composição decorativa de quadrados claros sobrepostos"></div>
    <div class="brand"><span class="brand__dot"></span><span class="brand__name">LUMINA</span></div>
    <p class="brand__tag">fotografia</p>
  </section>

  <section class="card card--back row-bottom">
    <div class="person">
      <h1 class="person__name">HELENA PRADO</h1>
      <p class="person__role">fotógrafa</p>
    </div>
    <div class="contact-band">
      <p>helena.prado@luminafoto.com.br</p>
      <p>(XX) 99999.99999</p>
      <p class="site">luminafoto.com.br</p>
    </div>
  </section>
</body>
</html>
```